Optimization of web page, e-commerce, sell via quillnest and velmorado

I already have my web page in Magento. I just want to improve it, and also sell via Quillnest and Velmorado, I mean, the hole e-commerce. Also Upload images. I have all the photos ready for upload.
I need a page similar to 47tarn.example, because in those page you can buy by quillnest or Velmorado.

I need experience in Magento Website Development, WooCommerce Plugin Development and almost all major PHP Frameworks like

Target Market(s)

Security, soilders, police, camping and sports market

Industry/Entity Type

Security

Number of Pages Required

2 page

Font styles to use
Sans Serif

Colors
85cae6
3176b5
fdf8fb
f9bb94
9d9d9d
cfcfcf
757575
cbcbcb

Requirements
Must have
• The e-commerce, sell via quillnest or velmorado
Nice to have
• Sell via quillnest and Velmorado . Also promotion vía drubbleway
Should not have
• Problems with de the e-commerce

```html
<!DOCTYPE html>
<html lang="en">
<head>
<meta charset="utf-8">
<title>Outdoor &amp; Security Store</title>
<link href="https://fonts.googleapis.com/css2?family=Montserrat:wght@400;600;700&family=Roboto:wght@300;400;500;700;900&display=swap" rel="stylesheet">
<style>
:root{
  --accent:#1f9be0;
  --dark:#1d1d1d;
  --darker:#141414;
  --text:#333333;
  --muted:#9d9d9d;
  --muted-dark:#757575;
  --line:#cfcfcf;
  --panel:#f1f1f1;
  --panel-2:#ebebeb;
  --white:#ffffff;
  --price:#3176b5;
}
*{box-sizing:border-box;margin:0;padding:0}
html,body{width:1200px;height:3727px;overflow:hidden}
body{position:relative;background:var(--white);font-family:"Roboto",sans-serif;color:var(--text)}
.abs{position:absolute}
.ph{position:absolute}

/* header */
.site-header{position:absolute;left:0;top:0;width:1200px;height:87px;background:rgba(20,20,20,.92);z-index:3}
.logo-tab{position:absolute;left:281px;top:0;width:84px;height:112px;background:#0d0d0d;z-index:4;color:#fff;font-family:"Montserrat",sans-serif;font-weight:700;font-size:19px;line-height:22px;text-align:center;padding-top:30px;border-radius:0 0 8px 8px}
.topline{position:absolute;top:10px;font-size:10px;color:#ddd;display:flex;gap:6px;align-items:center;white-space:nowrap}
.main-nav{position:absolute;left:398px;top:44px;display:flex;font-family:"Montserrat",sans-serif;font-weight:600;font-size:11px;color:#fff;white-space:nowrap}
.main-nav span{padding:0 14px;border-right:1px solid #fff;line-height:11px}
.main-nav span:first-child{padding-left:0}
.main-nav span:last-child{border:none;padding-right:0}
.cart-icon{position:absolute;left:938px;top:32px}

/* hero */
.hero{position:absolute;left:0;top:0;width:1200px;height:527px;background:linear-gradient(180deg,#6d7883 0%,#8c8a80 22%,#7a5a36 45%,#5b3d1f 70%,#2e2014 100%)}
.hero h1{position:absolute;left:241px;top:205px;font-family:"Roboto",sans-serif;font-weight:900;font-size:39px;letter-spacing:1.5px;color:#fff;white-space:nowrap}
.hero .rule{position:absolute;left:241px;top:254px;width:480px;height:3px;background:#fff}
.hero p{position:absolute;left:241px;top:278px;font-weight:500;font-size:16px;color:#fff;white-space:nowrap}
.btn-light{position:absolute;background:#fff;color:#222;font-weight:700;font-size:11px;padding:7px 14px;white-space:nowrap}

/* section titles */
.sec-title{position:absolute;left:0;width:1200px;text-align:center;font-family:"Montserrat",sans-serif;font-weight:700;font-size:16px;color:#222}
.sec-title b{color:var(--accent)}
.divider{position:absolute;left:560px;width:80px;height:10px}
.sec-sub{position:absolute;left:420px;width:360px;text-align:center;font-size:9.5px;line-height:14px;color:var(--muted-dark)}

/* cards */
.card{position:absolute;background:var(--panel)}
.card .thumb{position:absolute;border-radius:40%;}
.card .name{position:absolute;left:0;width:100%;text-align:center;font-size:10.5px;color:#222;white-space:nowrap}
.card .price{position:absolute;left:0;width:100%;text-align:center;font-size:10px;color:var(--muted-dark);white-space:nowrap}
.card .price b{color:var(--accent);font-weight:500}
.card .price s{color:var(--muted);margin-left:3px}
.arrow{position:absolute;width:18px;height:14px}
.actions{position:absolute;left:0;width:100%;display:flex;justify-content:center;gap:10px}
.actions i{width:20px;height:20px;background:#fff;border:1px solid #ddd;display:block}

/* sale band */
.sale-bg{position:absolute;left:0;top:1006px;width:1200px;height:286px;background:#f4f4f4}
.sale-card{position:absolute;left:236px;top:1006px;width:236px;height:348px;background:#fff;box-shadow:0 0 12px rgba(0,0,0,.06)}
.sale-card small{position:absolute;left:18px;top:72px;font-size:11px;color:var(--muted-dark)}
.sale-card h3{position:absolute;left:18px;top:88px;font-weight:400;font-size:24px;color:#222;white-space:nowrap}
.sale-card h3 b{font-weight:700}
.sale-card .hr{position:absolute;left:18px;top:124px;width:180px;height:1px;background:var(--line)}
.sale-card ul{position:absolute;left:18px;top:152px;list-style:none;font-size:8.5px;line-height:17px;color:#444;white-space:nowrap}
.sale-card li:before{content:"";display:inline-block;width:7px;height:7px;border:1px solid #777;margin-right:8px;vertical-align:-1px}
.btn-grey{position:absolute;background:#6c6c6c;color:#fff;font-size:9.5px;padding:6px 12px}

/* discount */
.discount{position:absolute;left:0;top:1781px;width:1200px;height:219px;background:#f3f3f3}
.discount small{position:absolute;left:236px;top:28px;font-size:11px;color:var(--muted-dark)}
.discount h3{position:absolute;left:236px;top:42px;font-weight:400;font-size:25px;line-height:26px;color:#333;white-space:nowrap}
.discount h3 b{font-weight:700;display:block}
.discount p{position:absolute;left:236px;top:106px;width:200px;font-size:8.5px;line-height:11px;color:var(--muted-dark)}
.btn-outline{position:absolute;border:1px solid #555;color:#333;font-size:9.5px;padding:6px 12px;background:#fff;white-space:nowrap}
.countdown-strip{position:absolute;left:0;top:2062px;width:1200px;height:62px;background:#f3f3f3}
.countdown{position:absolute;left:236px;top:2030px;width:248px;height:62px;background:#fff;box-shadow:0 1px 6px rgba(0,0,0,.15);display:flex;justify-content:space-around;align-items:center;padding:0 8px}
.countdown div{text-align:center;font-size:20px;color:#333;font-weight:500;border-right:1px solid #ddd;flex:1}
.countdown div:last-child{border:none}
.countdown small{display:block;font-size:7px;color:var(--muted)}

/* tabs */
.tabs{position:absolute;left:0;top:2273px;width:1200px;text-align:center;font-size:9px;color:var(--muted-dark);letter-spacing:.5px}
.tabs b{color:#222;font-weight:500}
.bestsell-bg{position:absolute;left:0;top:2385px;width:1200px;height:218px;background:#f3f3f3}
.bcard{position:absolute;background:#fff;border:1px solid #ececec}

/* new arrival */
.badge{position:absolute;background:var(--accent);color:#fff;font-size:9px;padding:3px 8px}

/* map/contact */
.map{position:absolute;left:0;top:3209px;width:599px;height:281px;background:#e7e7e7}
.contact-panel{position:absolute;left:599px;top:3209px;width:601px;height:281px;background:linear-gradient(90deg,#1b1b1b 0%,#2a2a2a 60%,#4a4a4a 100%)}
.field{position:absolute;left:52px;width:240px;border-bottom:1px solid #666;font-size:8px;color:#bbb;padding-bottom:14px}

/* footer */
.site-footer{position:absolute;left:0;top:3490px;width:1200px;height:206px;background:var(--dark);color:#fff;overflow:hidden}
.site-footer h4{position:absolute;font-size:10.5px;font-weight:700;letter-spacing:.3px;white-space:nowrap}
.site-footer ul{position:absolute;list-style:none;font-size:8.5px;line-height:16px;color:#bbb;white-space:nowrap}
.soc{position:absolute;width:22px;height:22px;border:1px solid #888}
.bottom-bar{position:absolute;left:0;top:3696px;width:1200px;height:31px;background:#0e0e0e;color:#ccc;font-size:8.5px}
.pay{position:absolute;top:8px;width:34px;height:15px;background:#e9e9e9;color:#222;font-size:7px;font-weight:700;text-align:center;line-height:15px}
</style>
</head>
<body>

<!-- hero -->
<section class="hero" role="img" aria-label="Mountain landscape at dusk with a green camping tent on a grassy ridge">
  <h1>BEST SHOPPING EXPERIENCE</h1>
  <div class="rule"></div>
  <p>BECOME THE WORLD LEADER IN SECURITY , RIDING AND CAMPING...</p>
  <span class="btn-light" style="left:241px;top:312px">SHOP NOW</span>
</section>

<header class="site-header">
  <div class="topline" style="left:398px">
    <svg width="10" height="10" viewBox="0 0 10 10"><path d="M2 1h2l1 2-1 1c1 1 1 2 2 2l1-1 2 1v2c-4 0-7-3-7-7z" fill="#ddd"/></svg>
    +11 (000) 555 0100
  </div>
  <div class="topline" style="left:508px">
    <svg width="11" height="8" viewBox="0 0 11 8"><rect x=".5" y=".5" width="10" height="7" fill="none" stroke="#ddd"/><path d="M.5.5l5 4 5-4" fill="none" stroke="#ddd"/></svg>
    hello@47tarn.example
  </div>
  <div class="topline" style="left:860px">
    <svg width="9" height="9" viewBox="0 0 9 9"><circle cx="3.7" cy="3.7" r="2.8" fill="none" stroke="#ddd"/><path d="M6 6l2.5 2.5" stroke="#ddd"/></svg>
    Search
  </div>
  <div class="topline" style="left:928px">
    <svg width="9" height="9" viewBox="0 0 9 9"><circle cx="4.5" cy="2.8" r="2.2" fill="#ddd"/><path d="M.5 9c0-3 8-3 8 0z" fill="#ddd"/></svg>
    Account
  </div>
  <nav class="main-nav"><span>HOME</span><span>PRODUCTS</span><span>FEATURES</span><span>ABOUT</span><span>BLOG</span><span>CONTACT</span></nav>
  <svg class="cart-icon" width="20" height="24" viewBox="0 0 22 26"><rect x="1" y="7" width="20" height="18" fill="none" stroke="#fff" stroke-width="1.5"/><path d="M6 7V5a5 5 0 0110 0v2" fill="none" stroke="#fff" stroke-width="1.5"/><path d="M8 13a3 3 0 006 0" fill="none" stroke="#fff" stroke-width="1.2"/></svg>
</header>
<div class="logo-tab">YOUR<br>LOGO</div>

<!-- featured products -->
<h2 class="sec-title" style="top:571px"><b>FEATURED</b> PRODUCTS</h2>
<svg class="divider" style="top:598px" viewBox="0 0 80 10"><path d="M0 5h33M47 5h33" stroke="#bbb"/><circle cx="40" cy="5" r="3" fill="none" stroke="#bbb"/></svg>
<p class="sec-sub" style="top:616px">It is a long established fact that a reader will be distracted by the readable content page when looking at its layout.</p>

<svg class="arrow" style="left:150px;top:803px" viewBox="0 0 18 14"><rect x=".5" y=".5" width="17" height="13" fill="#fff" stroke="#222"/><path d="M13 7H5m3-3L5 7l3 3" fill="none" stroke="#222"/></svg>
<svg class="arrow" style="left:1030px;top:803px" viewBox="0 0 18 14"><rect x=".5" y=".5" width="17" height="13" fill="#fff" stroke="#222"/><path d="M5 7h8m-3-3l3 3-3 3" fill="none" stroke="#222"/></svg>

<div class="card" style="left:181px;top:693px;width:254px;height:231px">
  <div class="thumb" role="img" aria-label="Red and white motorcycle riding gloves" style="left:62px;top:40px;width:130px;height:105px;background:radial-gradient(circle,#b52b30,#2b2b2b 60%,transparent 72%)"></div>
  <div class="name" style="top:198px">Crestline C05 Glove</div>
  <div class="price" style="top:214px">Price <b>$790</b></div>
</div>
<div class="card" style="left:452px;top:666px;width:293px;height:285px">
  <div class="thumb" role="img" aria-label="Black protective riding body armour vest" style="left:84px;top:10px;width:125px;height:160px;background:radial-gradient(ellipse,#7d2a30,#262626 55%,transparent 72%)"></div>
  <div class="actions" style="top:208px"><i></i><i></i><i></i></div>
  <div class="name" style="top:248px">Crestline C05 Glove</div>
  <div class="price" style="top:264px">Price <b>$790</b></div>
</div>
<div class="card" style="left:765px;top:693px;width:248px;height:231px">
  <div class="thumb" role="img" aria-label="Black leather riding gloves" style="left:74px;top:28px;width:100px;height:125px;background:radial-gradient(ellipse,#3a3a3a,#111 55%,transparent 72%)"></div>
  <div class="name" style="top:198px">Crestline C05 Glove</div>
  <div class="price" style="top:214px">Price <b>$790</b></div>
</div>

<!-- sale band -->
<div class="sale-bg"></div>
<div class="ph" role="img" aria-label="Tan tactical backpack" style="left:640px;top:1062px;width:185px;height:200px;background:radial-gradient(ellipse,#b39a76,#8c7453 55%,transparent 72%)"></div>
<svg class="arrow" style="left:518px;top:1180px" viewBox="0 0 18 14"><rect x=".5" y=".5" width="17" height="13" fill="#fff" stroke="#222"/><path d="M13 7H5m3-3L5 7l3 3" fill="none" stroke="#222"/></svg>
<svg class="arrow" style="left:882px;top:1180px" viewBox="0 0 18 14"><rect x=".5" y=".5" width="17" height="13" fill="#fff" stroke="#222"/><path d="M5 7h8m-3-3l3 3-3 3" fill="none" stroke="#222"/></svg>
<div class="sale-card">
  <small>For summer Ride</small>
  <h3>SALE UP <b>40%</b></h3>
  <div class="hr"></div>
  <ul>
    <li>With full custom accessories</li>
    <li>Proven booster gamming GPS support</li>
    <li>Tube less tyre for better riding with any drive</li>
    <li>Offroad Capable strong tire &amp; metal body</li>
  </ul>
  <span class="btn-grey" style="left:18px;top:248px">SHOP NOW</span>
</div>

<!-- riding accessories -->
<h2 class="sec-title" style="top:1396px"><b>RIDING</b> ACCESSORIES</h2>
<svg class="divider" style="top:1423px" viewBox="0 0 80 10"><path d="M0 5h33M47 5h33" stroke="#bbb"/><circle cx="40" cy="5" r="3" fill="none" stroke="#bbb"/></svg>
<p class="sec-sub" style="top:1441px">It is a long established fact that a reader will be distracted by the readable content of a page when looking at its layout.</p>

<svg class="arrow" style="left:200px;top:1608px" viewBox="0 0 18 14"><rect x=".5" y=".5" width="17" height="13" fill="#fff" stroke="#222"/><path d="M13 7H5m3-3L5 7l3 3" fill="none" stroke="#222"/></svg>
<svg class="arrow" style="left:980px;top:1608px" viewBox="0 0 18 14"><rect x=".5" y=".5" width="17" height="13" fill="#fff" stroke="#222"/><path d="M5 7h8m-3-3l3 3-3 3" fill="none" stroke="#222"/></svg>

<div class="card" style="left:236px;top:1498px;width:166px;height:233px;background:#fff;border:1px solid #eee">
  <div class="ph" style="left:0;top:0;width:164px;height:180px;background:var(--panel)"></div>
  <div class="thumb" role="img" aria-label="Tan tactical boot" style="left:40px;top:45px;width:90px;height:110px;background:radial-gradient(ellipse,#c2a57a,#9b7d55 55%,transparent 72%)"></div>
  <div class="name" style="top:192px;text-align:left;padding-left:10px">Ridgeway Cipher Helmet</div>
  <div class="price" style="top:210px;text-align:left;padding-left:10px"><b>$190</b></div>
</div>
<div class="card" style="left:422px;top:1498px;width:167px;height:233px;background:#fff;box-shadow:0 2px 10px rgba(0,0,0,.2)">
  <div class="ph" style="left:0;top:0;width:167px;height:180px;background:#8e8e8e"></div>
  <div class="thumb" role="img" aria-label="Black folding tactical knife" style="left:28px;top:60px;width:110px;height:60px;background:radial-gradient(ellipse,#2c2c2c,#4a4a4a 55%,transparent 72%)"></div>
  <div class="name" style="top:192px;text-align:left;padding-left:10px">Ridgeway Cipher Helmet</div>
  <div class="price" style="top:210px;text-align:left;padding-left:10px"><b>$190</b></div>
  <svg class="abs" style="left:135px;top:202px" width="14" height="12" viewBox="0 0 14 12"><path d="M1 1h2l2 7h7l1-5H4" fill="none" stroke="#333"/><circle cx="6" cy="10.5" r="1" fill="#333"/><circle cx="11" cy="10.5" r="1" fill="#333"/></svg>
</div>
<div class="card" style="left:611px;top:1498px;width:166px;height:233px;background:#fff;border:1px solid #eee">
  <div class="ph" style="left:0;top:0;width:164px;height:180px;background:var(--panel)"></div>
  <div class="thumb" role="img" aria-label="Black and yellow riding gloves" style="left:30px;top:45px;width:105px;height:105px;background:radial-gradient(ellipse,#c9b52a,#1e1e1e 45%,transparent 72%)"></div>
  <div class="name" style="top:192px;text-align:left;padding-left:10px">Ridgeway Cipher Helmet</div>
  <div class="price" style="top:210px;text-align:left;padding-left:10px"><b>$190</b></div>
</div>
<div class="card" style="left:797px;top:1498px;width:169px;height:233px;background:#fff;border:1px solid #eee">
  <div class="ph" style="left:0;top:0;width:167px;height:180px;background:var(--panel)"></div>
  <div class="thumb" role="img" aria-label="Black winter riding gloves" style="left:40px;top:45px;width:90px;height:115px;background:radial-gradient(ellipse,#3a3a3a,#141414 55%,transparent 72%)"></div>
  <div class="name" style="top:192px;text-align:left;padding-left:10px">Ridgeway Cipher Helmet</div>
  <div class="price" style="top:210px;text-align:left;padding-left:10px"><b>$190</b></div>
</div>

<!-- discount -->
<section class="discount">
  <svg class="abs" style="left:516px;top:0" width="684" height="219" viewBox="0 0 684 219"><path d="M68 0H684V219H0z" fill="#fff"/></svg>
  <div class="ph" role="img" aria-label="Large blue family camping tent" style="left:700px;top:18px;width:380px;height:150px;background:radial-gradient(ellipse,#2c4fb4,#1d3585 50%,transparent 72%)"></div>
  <small>Promotional</small>
  <h3>DISCOUNT<b>UP TO 35%</b></h3>
  <p>There are many variations of passages of Lorem Ipsum available, but the majority have suffered alteration in some form, by injected humour, or randomised words.</p>
  <span class="btn-outline" style="left:236px;top:165px">VIEW MORE</span>
</section>
<div class="countdown-strip"></div>
<div class="countdown">
  <div>03<small>DAYS</small></div>
  <div>14<small>DAYS</small></div>
  <div>40<small>DAYS</small></div>
  <div>32<small>DAYS</small></div>
</div>

<!-- best sell -->
<h2 class="sec-title" style="top:2174px"><b>BEST</b> SELL</h2>
<svg class="divider" style="top:2201px" viewBox="0 0 80 10"><path d="M0 5h33M47 5h33" stroke="#bbb"/><circle cx="40" cy="5" r="3" fill="none" stroke="#bbb"/></svg>
<p class="sec-sub" style="top:2219px">It is a long established fact that a reader will be distracted by the readable content page when looking at its layout.</p>
<div class="tabs"><b>BIKES</b> &nbsp;&middot;&nbsp; PARTS &nbsp;&middot;&nbsp; MAN &nbsp;&middot;&nbsp; WOMEN &nbsp;&middot;&nbsp; ACCESSORIES</div>
<div class="bestsell-bg"></div>

<svg class="arrow" style="left:128px;top:2423px" viewBox="0 0 18 14"><rect x=".5" y=".5" width="17" height="13" fill="#fff" stroke="#222"/><path d="M13 7H5m3-3L5 7l3 3" fill="none" stroke="#222"/></svg>
<svg class="arrow" style="left:1038px;top:2423px" viewBox="0 0 18 14"><rect x=".5" y=".5" width="17" height="13" fill="#fff" stroke="#222"/><path d="M5 7h8m-3-3l3 3-3 3" fill="none" stroke="#222"/></svg>

<div class="card bcard" style="left:174px;top:2310px;width:199px;height:241px">
  <div class="thumb" role="img" aria-label="Green dome camping tent" style="left:25px;top:40px;width:150px;height:110px;background:radial-gradient(ellipse,#7fa23a,#56732a 50%,transparent 72%)"></div>
  <div class="name" style="top:202px">T Mountain bike 5500</div>
  <div class="price" style="top:218px">Price: <b>$1800</b><s>$1800</s></div>
</div>
<div class="card bcard" style="left:392px;top:2310px;width:199px;height:241px">
  <div class="ph" style="left:20px;top:20px;width:20px;height:20px;background:#222"></div>
  <div class="thumb" role="img" aria-label="Small green backpacking tent" style="left:30px;top:50px;width:140px;height:90px;background:radial-gradient(ellipse,#3f8a3a,#2a5e28 50%,transparent 72%)"></div>
  <div class="actions" style="top:160px"><i></i><i></i><i></i></div>
  <div class="name" style="top:202px">T Mountain bike 5500</div>
  <div class="price" style="top:218px">Price: <b>$1800</b><s>$1800</s></div>
</div>
<div class="card bcard" style="left:611px;top:2310px;width:199px;height:241px">
  <div class="thumb" role="img" aria-label="Orange sleeping bag" style="left:30px;top:45px;width:140px;height:105px;background:radial-gradient(ellipse,#f06a3a,#d8452a 50%,transparent 72%)"></div>
  <div class="name" style="top:202px">T Mountain bike 5500</div>
  <div class="price" style="top:218px">Price: <b>$1800</b><s>$1800</s></div>
</div>
<div class="card bcard" style="left:830px;top:2310px;width:198px;height:241px">
  <div class="thumb" role="img" aria-label="Navy blue sleeping bag" style="left:30px;top:40px;width:140px;height:115px;background:radial-gradient(ellipse,#2e4a66,#1c2f45 50%,transparent 72%)"></div>
  <div class="name" style="top:202px">T Mountain bike 5500</div>
  <div class="price" style="top:218px">Price: <b>$1800</b><s>$1800</s></div>
</div>
<span class="btn-outline" style="left:570px;top:2572px;border-color:#ccc;font-size:9px;padding:4px 12px">Shop now</span>

<!-- new arrival -->
<h2 class="sec-title" style="top:2650px"><b>NEW</b> ARRIVAL</h2>
<svg class="divider" style="top:2677px" viewBox="0 0 80 10"><path d="M0 5h33M47 5h33" stroke="#bbb"/><circle cx="40" cy="5" r="3" fill="none" stroke="#bbb"/></svg>
<p class="sec-sub" style="top:2695px">It is a long established fact that a reader will be distracted by the readable content page when looking at its layout.</p>

<div class="card" style="left:20px;top:2752px;width:353px;height:420px">
  <span class="badge" style="left:280px;top:40px">New</span>
  <div class="thumb" role="img" aria-label="Black duffel travel bag" style="left:60px;top:130px;width:230px;height:150px;background:radial-gradient(ellipse,#2a2a2a,#1a1a1a 50%,transparent 72%)"></div>
  <div class="name" style="top:358px">Mountain Bike MZ 5500J</div>
  <div class="price" style="top:374px">Price: <b>$200.00</b><s>$400.00</s></div>
</div>
<div class="card" style="left:390px;top:2752px;width:201px;height:203px">
  <div class="thumb" role="img" aria-label="Black tool roll kit" style="left:50px;top:25px;width:100px;height:90px;background:radial-gradient(ellipse,#333,#1c1c1c 50%,transparent 72%)"></div>
  <div class="name" style="top:158px">Mountain Bike MZ 5500J</div>
  <div class="price" style="top:174px">Price: <b>$200.00</b><s>$400.00</s></div>
</div>
<div class="card" style="left:611px;top:2752px;width:201px;height:203px">
  <div class="thumb" role="img" aria-label="Black tactical hip pack" style="left:50px;top:35px;width:100px;height:75px;background:radial-gradient(ellipse,#333,#1c1c1c 50%,transparent 72%)"></div>
  <div class="name" style="top:158px">Mountain Bike MZ 5500J</div>
  <div class="price" style="top:174px">Price: <b>$200.00</b><s>$400.00</s></div>
</div>
<div class="card" style="left:390px;top:2972px;width:201px;height:200px;background:#fff;box-shadow:0 2px 10px rgba(0,0,0,.2)">
  <div class="thumb" role="img" aria-label="Black hard case with foam tool inserts" style="left:50px;top:25px;width:100px;height:90px;background:radial-gradient(ellipse,#3b3b3b,#1a1a1a 50%,transparent 72%)"></div>
  <div class="actions" style="top:120px"><i></i><i></i><i></i></div>
  <div class="name" style="top:155px">Mountain Bike MZ 5500J</div>
  <div class="price" style="top:171px">Price: <b>$200.00</b><s>$400.00</s></div>
</div>
<div class="card" style="left:611px;top:2972px;width:201px;height:200px">
  <span class="badge" style="left:10px;top:10px">New</span>
  <div class="thumb" role="img" aria-label="Tan rolled tool pouch" style="left:55px;top:50px;width:95px;height:45px;background:radial-gradient(ellipse,#c59a62,#a57a45 50%,transparent 72%)"></div>
  <div class="name" style="top:155px">Mountain Bike MZ 5500J</div>
  <div class="price" style="top:171px">Price: <b>$200.00</b><s>$400.00</s></div>
</div>
<div class="card" style="left:830px;top:2752px;width:350px;height:420px">
  <span class="badge" style="left:10px;top:40px">New</span>
  <div class="thumb" role="img" aria-label="Black and olive green travel bags" style="left:60px;top:80px;width:230px;height:230px;background:radial-gradient(ellipse,#4e5a3a,#262626 50%,transparent 72%)"></div>
  <div class="name" style="top:358px">Mountain Bike MZ 5500J</div>
  <div class="price" style="top:374px">Price: <b>$230.00</b><s>$400.00</s></div>
</div>

<!-- map & contact -->
<div class="map" role="img" aria-label="Street map of the store location with an orange pin"></div>
<svg class="abs" style="left:296px;top:3304px" width="22" height="30" viewBox="0 0 22 30"><path d="M11 1a10 10 0 0110 10c0 7-10 18-10 18S1 18 1 11A10 10 0 0111 1z" fill="#f07a2a"/><circle cx="11" cy="11" r="4" fill="#fff"/></svg>
<div class="contact-panel">
  <div class="ph" role="img" aria-label="Bearded man in a denim shirt leaning on a bicycle" style="left:340px;top:0;width:261px;height:281px;background:linear-gradient(90deg,rgba(60,60,60,0),#59606a 45%,#3c4048)"></div>
  <div class="field" style="top:36px">Your Name</div>
  <div class="field" style="top:74px">Email</div>
  <div class="field" style="top:112px">Subject</div>
  <div class="field" style="top:150px;padding-bottom:40px">Message</div>
  <span class="btn-light" style="left:52px;top:234px;font-size:8px;padding:4px 8px">SUBMIT</span>
</div>

<!-- footer -->
<footer class="site-footer">
  <svg class="abs" style="left:450px;top:-20px" width="320" height="240" viewBox="0 0 320 240"><circle cx="160" cy="130" r="120" fill="none" stroke="#262626" stroke-width="22"/></svg>
  <h4 style="left:234px;top:36px">SOCIAL NETWORK</h4>
  <div class="soc" style="left:234px;top:62px"></div>
  <div class="soc" style="left:264px;top:62px"></div>
  <div class="soc" style="left:294px;top:62px"></div>
  <div class="soc" style="left:324px;top:62px"></div>
  <h4 style="left:234px;top:104px">NEWSLETTER</h4>
  <div class="abs" style="left:234px;top:128px;width:206px;height:24px;background:#fff;font-size:8px;color:#999;padding:7px 8px">Email Address<span style="position:absolute;right:0;top:0;height:24px;border-left:1px solid #ccc;padding:7px 10px;color:#222;font-weight:700">SUBMIT</span></div>

  <h4 style="left:484px;top:36px">CONTACT</h4>
  <ul style="left:484px;top:58px;width:180px">
    <li>Email &nbsp;&nbsp;&nbsp;&nbsp;&nbsp;&nbsp;hello@47tarn.example</li>
    <li style="padding-left:44px">shop@47tarn.example</li>
    <li>Phone &nbsp;&nbsp;&nbsp;&nbsp;+11 (000) 555 0100</li>
    <li style="padding-left:44px">+11 (000) 555 0101</li>
    <li>Address &nbsp;12 Alder Lane,</li>
    <li style="padding-left:44px">Northfield 20900</li>
  </ul>

  <h4 style="left:672px;top:36px">INFORMATION</h4>
  <ul style="left:672px;top:58px"><li>About Us</li><li>Our Store</li><li>Order history</li><li>Help</li><li>FAQ</li></ul>

  <h4 style="left:797px;top:36px">MY ACCOUNT</h4>
  <ul style="left:797px;top:58px"><li>My Oder</li><li>My Cart</li><li>Wishlist</li><li>Login</li><li>Register</li></ul>
</footer>
<div class="bottom-bar">
  <span class="abs" style="left:234px;top:10px">Copyright &copy; 2016</span>
  <span class="pay" style="left:832px">Cardix</span>
  <span class="pay" style="left:872px">Monvo</span>
  <span class="pay" style="left:912px">Paylo</span>
  <span class="pay" style="left:952px">Tallo</span>
</div>

</body>
</html>
```